General brochure with course listing

A general brochure for the Global Statute Academy, about 40 A5 pages that includes mission, vision, history, descriptions of our technical assistance and capacity building programming and detailed descriptions of our courses. Would be for both online pdf (magazine style) and print. I have attached an example of an older one that was satisfactory but not as professional as what we're looking for now.

Target Market(s)

Lawyers and government officials around the world.

Industry/Entity Type

Legal and capacity building

Requirements
Must have
• A good design and template that we can replicate on our own in InDesign annually. We need the layout from you and we will provide the copy. We will also publish as a pdf
Nice to have
• Colors and branding from our website - www.gsa-learn.org

```html
<!DOCTYPE html>
<html lang="en">
<head>
<meta charset="utf-8">
<title>Global Statute Academy — 2024 Announcement of Programs</title>
<link href="https://fonts.googleapis.com/css2?family=Montserrat:wght@400;500;800&display=swap" rel="stylesheet">
<style>
  :root {
    --stage-blue: #3f58a8;
    --panel-blue: #3552a3;
    --navy: #1c2350;
    --orange: #e4642f;
    --white: #ffffff;
    --photo-dark: #1e2748;
    --photo-mid: #3b4f8f;
    --photo-light: #7c8fc4;
  }
  * { margin: 0; padding: 0; box-sizing: border-box; }
  html, body {
    width: 1200px;
    height: 700px;
    overflow: hidden;
    background: var(--stage-blue);
    font-family: "Montserrat", sans-serif;
  }
  .cover {
    position: absolute;
    left: 160px;
    top: 40px;
    width: 880px;
    height: 620px;
    overflow: hidden;
    box-shadow: 0 18px 40px rgba(10, 20, 60, 0.35);
  }
  .cover-photo {
    position: absolute;
    inset: 0;
    background:
      radial-gradient(ellipse at 62% 22%, rgba(210, 170, 150, 0.45), transparent 30%),
      radial-gradient(ellipse at 22% 55%, rgba(190, 150, 130, 0.35), transparent 28%),
      linear-gradient(160deg, var(--photo-dark) 0%, var(--photo-mid) 45%, var(--photo-light) 70%, var(--photo-dark) 100%);
  }
  .mosaic-tile {
    position: absolute;
    background: rgba(70, 110, 200, 0.35);
  }
  .mosaic-tile.orange { background: rgba(228, 100, 47, 0.88); }
  .mosaic-tile.pale { background: rgba(150, 180, 235, 0.28); }
  .brand-tile {
    position: absolute;
    left: 120px;
    top: 70px;
    width: 150px;
    height: 150px;
    background: var(--white);
    display: flex;
    flex-direction: column;
    align-items: center;
    justify-content: center;
    gap: 10px;
  }
  .brand-mark {
    width: 14px;
    height: 14px;
    border-radius: 50%;
    background: var(--navy);
  }
  .brand-name {
    color: var(--navy);
    font-weight: 800;
    font-size: 15px;
    line-height: 1.2;
    text-align: center;
    letter-spacing: 0.04em;
    text-transform: uppercase;
  }
  .title-panel {
    position: absolute;
    left: 430px;
    top: 260px;
    width: 450px;
    height: 230px;
    background: var(--panel-blue);
    padding: 26px 0 0 44px;
  }
  .year-tag {
    display: inline-block;
    background: var(--orange);
    color: var(--navy);
    font-weight: 800;
    font-size: 18px;
    letter-spacing: 0.08em;
    padding: 4px 16px;
    margin-bottom: 12px;
  }
  .cover-title {
    color: var(--white);
    font-weight: 800;
    font-size: 34px;
    line-height: 1.08;
    letter-spacing: 0.06em;
    text-transform: uppercase;
  }
  .cover-subtitle {
    margin-top: 12px;
    color: var(--white);
    font-weight: 500;
    font-size: 19px;
    line-height: 1.25;
  }
</style>
</head>
<body>
  <main class="cover">
    <div class="cover-photo" role="img" aria-label="Photo of lawyers and officials seated in a lecture hall, taking notes during a training session"></div>

    <div class="mosaic-tile" style="left:60px; top:300px; width:110px; height:110px;"></div>
    <div class="mosaic-tile pale" style="left:300px; top:360px; width:120px; height:120px;"></div>
    <div class="mosaic-tile orange" style="left:130px; top:420px; width:150px; height:150px;"></div>
    <div class="mosaic-tile" style="left:280px; top:480px; width:150px; height:140px;"></div>
    <div class="mosaic-tile pale" style="left:0; top:560px; width:130px; height:60px;"></div>

    <div class="brand-tile">
      <span class="brand-mark"></span>
      <span class="brand-name">Global<br>Statute<br>Academy</span>
    </div>

    <section class="title-panel">
      <span class="year-tag">2024</span>
      <h1 class="cover-title">Announcement<br>of Programs</h1>
      <p class="cover-subtitle">Training in Finance, Management,<br>Law and Governance</p>
    </section>
  </main>
</body>
</html>
```